DENTIST OFFICE POST CARD DESIGN

COMPANY NAME: BEARABLE DENTISTRYCome and see if Quillmoor Dentistry is for you.... ALWAYSWELCOMINGNEW PATIENTS!Call today for your appointment!607 555 0183 We are located on 7 Penwick Street , Oneonta, Ny----(map scketch)All in one stop for all your dental care needsCOSMETIC DENTISTRYDENTAL IMPLANTSROOT CANALSVENEERSWHITENINGSFILLINGSCROWNSBRIDGESDENTURESEXTRACTIONSGUM TREATMENTSSNAP ON SMILECOLOR------ANYPOSTCARD INDICIA;PRSRT STDECRWSSU.S. POSTAGEPAIDEDDM RETAILLocalPostal Customer

```html
<!DOCTYPE html>
<html lang="en">
<head>
<meta charset="utf-8">
<title>Quillmoor Dentistry Postcard</title>
<link href="https://fonts.googleapis.com/css2?family=Roboto+Condensed:wght@400&family=Lato:ital,wght@1,700;1,900&display=swap" rel="stylesheet">
<style>
  :root{
    --green-light:#a5d03f;
    --green-dark:#5fa52c;
    --blue:#1b8fd0;
    --ink:#1f1f1f;
    --black-band:#222222;
    --white:#ffffff;
    --page:#e9e9e9;
    --skin-light:#f1c6ae;
    --skin-dark:#d89a84;
    --map:#ececea;
  }
  *{margin:0;padding:0;box-sizing:border-box}
  html,body{width:1200px;height:902px;overflow:hidden;background:var(--page)}
  .postcard{
    position:absolute;left:20px;top:133px;width:1160px;height:636px;
    background:var(--white);overflow:hidden;
    box-shadow:0 2px 10px rgba(0,0,0,.15);
  }
  .postcard__shapes{position:absolute;inset:0}
  .brand-name{
    position:absolute;right:24px;top:32px;
    font-family:"Roboto Condensed",sans-serif;font-weight:400;
    font-size:66px;line-height:1;color:var(--ink);letter-spacing:.5px;
  }
  .invitation{
    position:absolute;right:26px;top:140px;text-align:right;
    font-family:"Lato",sans-serif;font-style:italic;font-weight:700;
    font-size:49px;line-height:63px;color:var(--blue);
  }
  .welcome{
    position:absolute;right:24px;top:315px;
    font-family:"Roboto Condensed",sans-serif;font-size:42px;line-height:1;
    color:var(--white);
  }
  .services__title{
    position:absolute;right:26px;top:398px;
    font-family:"Lato",sans-serif;font-style:italic;font-weight:900;
    font-size:27px;color:var(--ink);
  }
  .services__list{
    position:absolute;top:447px;list-style:none;
    font-family:"Lato",sans-serif;font-style:italic;font-weight:700;
    font-size:18px;color:var(--ink);text-align:right;
  }
  .services__list--left{right:437px}
  .services__list--right{right:28px}
  .services__list li{height:32px;line-height:32px}
  .services__list li::after{
    content:"";display:inline-block;width:14px;height:14px;border-radius:50%;
    background:var(--green-light);margin-left:18px;vertical-align:-1px;
  }
  .cta{
    position:absolute;left:340px;top:570px;
    font-family:"Lato",sans-serif;font-style:italic;font-weight:700;
    font-size:27px;color:var(--white);
  }
  .phone{position:absolute;right:30px;top:562px;display:flex;align-items:center;gap:22px}
  .phone__icon{width:40px;height:40px}
  .phone__number{
    font-family:"Lato",sans-serif;font-weight:700;font-style:normal;
    font-size:42px;color:var(--green-light);letter-spacing:.5px;
  }
  .location-map{
    position:absolute;left:2px;top:522px;width:320px;height:112px;
    border:3px solid var(--blue);border-radius:10px;background:var(--map);
  }
</style>
</head>
<body>
<div class="postcard">
  <svg class="postcard__shapes" viewBox="0 0 1160 636" width="1160" height="636">
    <defs>
      <linearGradient id="greenBand" x1="0" x2="1" y1="0" y2="0">
        <stop offset="0" stop-color="var(--green-light)" style="stop-color:#a5d03f"/>
        <stop offset="1" stop-color="#5fa52c"/>
      </linearGradient>
      <linearGradient id="skinTone" x1="0" x2="1" y1="0" y2="1">
        <stop offset="0" stop-color="#f3cdb7"/>
        <stop offset="1" stop-color="#d89a84"/>
      </linearGradient>
    </defs>
    <!-- top green band -->
    <path d="M0,0 H1160 V112 Q850,98 520,112 L0,112 Z" fill="url(#greenBand)"/>
    <path d="M510,113 Q850,96 1160,114" fill="none" stroke="#1f1f1f" stroke-width="3"/>
    <path d="M510,120 Q850,104 1160,121" fill="none" stroke="#1b8fd0" stroke-width="1.5"/>
    <!-- middle green band -->
    <path d="M380,293 H1160 V389 H330 Z" fill="url(#greenBand)"/>
    <!-- bottom black band -->
    <rect x="0" y="549" width="1160" height="87" fill="#222222"/>
    <rect x="0" y="546" width="1160" height="3" fill="#1b8fd0"/>
    <!-- photo area -->
    <path d="M0,0 H330 C430,40 480,140 440,235 C400,330 262,405 240,548 H0 Z" fill="url(#skinTone)" role="img" aria-label="Close-up photo of a smiling mouth with white teeth and a dental mirror"/>
    <!-- black swooshes -->
    <path d="M25,0 C140,28 260,44 390,30 C270,62 140,52 25,0 Z" fill="#1f1f1f"/>
    <path d="M262,548 C290,440 360,395 430,348 C380,410 320,460 300,548 Z" fill="#1f1f1f"/>
    <!-- blue swoosh -->
    <path d="M340,55 C475,110 475,235 405,330 C345,410 265,450 240,548" fill="none" stroke="#1b8fd0" stroke-width="24" stroke-linecap="round"/>
  </svg>

  <h1 class="brand-name">QUILLMOOR DENTISTRY</h1>
  <p class="invitation">Come and see if Quillmoor<br>Dentistry is for you....</p>
  <p class="welcome">ALWAYS WELCOMING NEW PATIENTS!</p>

  <section class="services">
    <h2 class="services__title">All in one stop for all your dental care needs</h2>
    <ul class="services__list services__list--left">
      <li>Cosmetic dentistrydental</li>
      <li>Implantsroot canalsveneers</li>
      <li>Whitenings</li>
    </ul>
    <ul class="services__list services__list--right">
      <li>Fillings crowns</li>
      <li>Bridges denturesextractionsgum</li>
      <li>Ttreatmentsglide in grincolor</li>
    </ul>
  </section>

  <div class="location-map" role="img" aria-label="Street map sketch showing the office at 7 Penwick Street"></div>

  <p class="cta">Call today for your appointment!</p>
  <div class="phone">
    <svg class="phone__icon" viewBox="0 0 40 40" aria-hidden="true">
      <circle cx="20" cy="20" r="20" fill="#ffffff"/>
      <path d="M14,11 l4,0 l2,6 l-3,2 c1.5,3 3,4.5 6,6 l2,-3 l6,2 l0,4 c-10,1 -18,-7 -17,-17 z" fill="#222222"/>
      <path d="M23,12 a6,6 0 0 1 5,5 M23,8 a10,10 0 0 1 9,9" fill="none" stroke="#222222" stroke-width="1.6"/>
    </svg>
    <span class="phone__number">607 555 0183</span>
  </div>
</div>
</body>
</html>
```